1 OZ TRANSDERMAL CBD. NOVEL, INNOVATIVE FIRST TIME EVER OF CBD THAT PENETRATES THROUGH SKIN.
BRAND: VELLOR WELLWORKS
NAME: HEMP GLIDE

Target Market(s)

CBD users waiting a smarter way-through the skin. None lost in toilet like other CBD, directly into you within 5 minutes.

Requirements
Must have
• Elegant, bold, natural, NOT THE SAME OLD CBD. Jump off shelf.
Should not have
• Boring "me-too" labels.

```html
<!DOCTYPE html>
<html lang="en">
<head>
<meta charset="UTF-8">
<title>Hemp Glide Label</title>
<link rel="stylesheet" href="https://fonts.googleapis.com/css2?family=Roboto+Condensed:wght@400;700&family=Montserrat:wght@400;600&display=swap">
<style>
  :root {
    --page: #f6f4f2;
    --label: #141414;
    --teal: #4cc3ce;
    --teal-band: #3fbdc9;
    --band-ink: #1b2b30;
    --badge: #2e7d87;
    --white: #ffffff;
    --molecule-a: #5a5d62;
    --molecule-b: #2a2b2e;
  }
  html, body {
    margin: 0;
    padding: 0;
    width: 1193px;
    height: 1200px;
    overflow: hidden;
    background: var(--page);
  }
  .label {
    position: absolute;
    left: 246px;
    top: 85px;
    width: 700px;
    height: 1030px;
    background: var(--label);
    color: var(--white);
  }
  .product-name {
    position: absolute;
    top: 14px;
    left: 0;
    width: 100%;
    margin: 0;
    text-align: center;
    font-family: "Roboto Condensed", sans-serif;
    font-weight: 400;
    font-size: 150px;
    line-height: 170px;
    color: var(--teal);
    letter-spacing: -1px;
  }
  .claim-band {
    position: absolute;
    top: 196px;
    left: 14px;
    width: 672px;
    height: 154px;
    background: var(--teal-band);
    display: flex;
    flex-direction: column;
    justify-content: center;
    align-items: center;
    font-family: "Montserrat", sans-serif;
    font-weight: 600;
    font-size: 50px;
    line-height: 70px;
    color: var(--band-ink);
    text-transform: uppercase;
  }
  .formula {
    position: absolute;
    top: 372px;
    left: 22px;
    margin: 0;
    font-family: "Montserrat", sans-serif;
    font-weight: 400;
    font-size: 47px;
    line-height: 74px;
    letter-spacing: 0.08em;
  }
  .molecule {
    position: absolute;
    left: 35px;
    top: 680px;
    width: 520px;
    height: 230px;
    border-radius: 14px;
    background: radial-gradient(ellipse at 45% 50%, var(--molecule-a), var(--molecule-b) 75%);
  }
  .strength-badge {
    position: absolute;
    left: 490px;
    top: 582px;
    width: 174px;
    height: 174px;
    border-radius: 50%;
    background: var(--badge);
    border: 6px solid var(--white);
    box-sizing: border-box;
    display: flex;
    flex-direction: column;
    justify-content: center;
    align-items: center;
    font-family: "Roboto Condensed", sans-serif;
    font-weight: 700;
    font-size: 66px;
    line-height: 64px;
  }
  .volume {
    position: absolute;
    top: 960px;
    left: 0;
    width: 100%;
    text-align: center;
    font-family: "Montserrat", sans-serif;
    font-weight: 600;
    font-size: 50px;
    line-height: 60px;
  }
</style>
</head>
<body>
  <main class="label">
    <h1 class="product-name">HEMP GLIDE</h1>
    <div class="claim-band">
      <span>Ultra-Fast Entry</span>
      <span>Through Skin</span>
    </div>
    <p class="formula">99% PURE CBD plus<br>Cross-linked 3-D<br>Hyaluronic Acid<br>Nanocarrier</p>
    <div class="molecule" role="img" aria-label="Ball-and-stick molecular structure of cannabidiol"></div>
    <div class="strength-badge">
      <span>2000</span>
      <span>mg</span>
    </div>
    <div class="volume">1fl. oz/30ml</div>
  </main>
</body>
</html>
```